Cowboy Ned
Cowboy Ned -
Professional
"Cowboy Ned" Hollins, Broker/Owner
Cowboy Ned Realty, LLC
4382 W Juniper Ridge Ln Gilbert, AZ 85297 (Address to be in smaller letters so as not to stand out)
Ned@CowboyNedRealty.example
www.CowboyNedRealty.example
Blog: http://housetalkhub.example/blogs/cowboyned Logo will be uploaded and should be on the front of the card. It may take up the whole front, or the front may include my phone and fax number. KTM, uDOM, FHLS, VOT Those designations above are to be added under my name.
The back will have possibly my head shot plus the contact information, web sites, etc and a couple of required Homeward logos scaled very small so as to hardly be noticeable.

```html
<!DOCTYPE html>
<html lang="en">
<head>
<meta charset="utf-8">
<title>Cowboy Ned Realty – Business Card</title>
<link rel="stylesheet" href="https://fonts.googleapis.com/css2?family=Cinzel:wght@500&family=PT+Sans:wght@400;700&display=swap">
<style>
  :root {
    --backdrop: #8e1a1c;
    --backdrop-light: #a52426;
    --card: #ffffff;
    --blue: #1b6fb5;
    --blue-dark: #175c98;
    --orange: #e08a1e;
    --gray: #8a8f96;
    --photo-a: #9aa3ad;
    --photo-b: #5a6470;
  }
  * { box-sizing: border-box; margin: 0; padding: 0; }
  html, body { width: 1200px; height: 901px; overflow: hidden; }
  body {
    background: radial-gradient(ellipse at center, var(--backdrop-light) 0%, var(--backdrop) 75%);
    font-family: "PT Sans", Arial, sans-serif;
    position: relative;
  }
  .card {
    position: absolute;
    left: 260px;
    width: 682px;
    height: 394px;
    background: var(--card);
    overflow: hidden;
    box-shadow: 0 2px 6px rgba(0,0,0,.25);
  }
  .card--front { top: 44px; }
  .card--back { top: 462px; }

  /* front */
  .band {
    position: absolute; left: 0; width: 100%;
    background: var(--blue);
  }
  .band--top { top: 6px; height: 36px; border-bottom: 4px solid var(--orange); }
  .band--bottom { bottom: 6px; height: 40px; border-top: 4px solid var(--orange); }
  .logo-mark {
    position: absolute; left: 36px; top: 106px;
    width: 182px; height: 182px; border-radius: 50%;
    border: 8px solid var(--orange);
  }
  .brand {
    position: absolute; left: 252px; top: 118px; width: 410px;
    text-align: center;
  }
  .brand__name {
    font-family: "Cinzel", Georgia, serif; font-weight: 500;
    color: var(--blue); font-size: 50px; line-height: 60px;
  }
  .brand__tagline {
    font-family: "Cinzel", Georgia, serif; font-weight: 500;
    color: var(--orange); font-size: 27px; letter-spacing: 3px;
    margin-top: 6px;
  }

  /* back */
  .headshot {
    position: absolute; left: 24px; top: 20px;
    width: 132px; height: 158px; border-radius: 10px;
    border: 3px solid var(--orange);
    background: linear-gradient(160deg, var(--photo-a), var(--photo-b));
  }
  .agent {
    position: absolute; left: 170px; top: 54px;
    color: var(--blue); font-size: 26px; line-height: 1;
    white-space: nowrap;
  }
  .agent__title { font-size: 19px; }
  .name-rule { position: absolute; left: 156px; top: 76px; }
  .mini-mark {
    position: absolute; right: 20px; top: 14px;
    width: 66px; height: 66px; border-radius: 50%;
    border: 4px solid var(--orange);
  }
  .designations {
    position: absolute; right: 30px; top: 124px;
    font-family: "Cinzel", Georgia, serif;
    color: var(--orange); font-size: 22px; letter-spacing: 3px;
  }
  .contact {
    position: absolute; left: 28px; top: 210px;
    list-style: none; color: var(--orange);
    font-size: 19px; line-height: 26px;
  }
  .footer-rule { position: absolute; left: 0; top: 334px; }
  .badges { position: absolute; left: 28px; top: 362px; display: flex; gap: 8px; }
  .badge { width: 16px; height: 12px; background: var(--gray); }
  .address {
    position: absolute; right: 26px; top: 360px;
    color: var(--gray); font-size: 14px;
  }
</style>
</head>
<body>

<section class="card card--front" aria-label="Card front">
  <div class="band band--top"></div>
  <div class="logo-mark"></div>
  <div class="brand">
    <div class="brand__name">COWBOY NED REALTY, LLC</div>
    <div class="brand__tagline">FIRST CLASS SERVICE</div>
  </div>
  <div class="band band--bottom"></div>
</section>

<section class="card card--back" aria-label="Card back">
  <div class="headshot" role="img" aria-label="Head shot of Cowboy Ned Hollins"></div>
  <p class="agent">“Cowboy Ned” Hollins, <span class="agent__title">Broker/Owner</span></p>
  <svg class="name-rule" width="510" height="30" viewBox="0 0 510 30">
    <path d="M0 20 H400 Q460 20 505 4" fill="none" stroke="var(--blue)" stroke-width="5"/>
    <path d="M0 26 H408 Q465 26 508 10" fill="none" stroke="var(--orange)" stroke-width="2"/>
  </svg>
  <div class="mini-mark"></div>
  <p class="designations">KTM, uDOM, FHLS, VOT</p>
  <ul class="contact">
    <li>Cell: (480) 555 0147</li>
    <li>Fax: (480) 555 0193</li>
    <li>Email: Ned@CowboyNedRealty.example</li>
    <li>Web: www.CowboyNedRealty.example</li>
    <li>Blog: http://housetalkhub.example/blogs/cowboyned</li>
  </ul>
  <svg class="footer-rule" width="682" height="20" viewBox="0 0 682 20">
    <path d="M0 14 H560 Q620 14 670 2" fill="none" stroke="var(--orange)" stroke-width="3"/>
    <path d="M60 18 H600 Q640 18 676 8" fill="none" stroke="var(--blue)" stroke-width="4"/>
  </svg>
  <div class="badges"><span class="badge"></span><span class="badge"></span></div>
  <p class="address">4382 W Juniper Ridge Ln :: Gilbert, AZ 85297</p>
</section>

</body>
</html>
```